Postcard Design

Mexican Grill quick service prepare to order fresh food. Website : www.casaverdekitchen.com.

A sample of a postcard for inspiration is attached.

Target Market(s)

University Students 20-30yrs old

Industry/Entity Type

It Service

```html
<!DOCTYPE html>
<html lang="en">
<head>
<meta charset="utf-8">
<title>Casa Verde Kitchen – Postcard</title>
<link rel="stylesheet" href="https://fonts.googleapis.com/css2?family=Jost:wght@400;500;700;800&family=Rye&family=Alfa+Slab+One&display=swap">
<style>
  :root {
    --page-bg: #2e2e30;
    --brand-red: #b5121b;
    --maroon: #7a1c1c;
    --charcoal: #3a3a3a;
    --fresh-green: #5aa02c;
    --white: #ffffff;
    --peach-light: #fbe3cf;
    --peach-mid: #f0c39c;
    --tan: #d9a36e;
  }
  * { margin: 0; padding: 0; box-sizing: border-box; }
  html, body { width: 1200px; height: 1200px; overflow: hidden; background: var(--page-bg); }
  .postcard {
    position: absolute; left: 40px; top: 237px; width: 1120px; height: 726px;
    overflow: hidden; font-family: "Jost", sans-serif;
  }
  .postcard__photo {
    position: absolute; inset: 0;
    background:
      radial-gradient(ellipse 45% 55% at 70% 72%, #e8cfa6 0%, #d8b27c 40%, rgba(216,178,124,0) 75%),
      radial-gradient(ellipse 30% 18% at 48% 35%, #f4ece4 0%, rgba(244,236,228,0) 80%),
      linear-gradient(100deg, var(--peach-light) 0%, #f7d5b7 40%, var(--peach-mid) 70%, var(--tan) 100%);
  }
  .brand {
    position: absolute; left: 62px; top: 100px; width: 390px;
    display: flex; align-items: center; gap: 16px;
  }
  .brand__dot { flex: none; width: 24px; height: 24px; border-radius: 50%; background: var(--brand-red); }
  .brand__name { font-weight: 800; font-size: 54px; color: var(--brand-red); line-height: 1.05; }
  .locator {
    position: absolute; right: 38px; top: 28px;
    font-weight: 500; font-size: 29px; color: var(--white);
  }
  .info-box {
    position: absolute; left: 471px; top: 82px; width: 610px; height: 128px;
    background: var(--brand-red); color: var(--white);
    border-radius: 6px; padding: 8px 18px;
  }
  .info-box__address { font-weight: 700; font-size: 23px; line-height: 1.2; }
  .info-box__center { font-size: 20px; line-height: 1.3; }
  .info-box__center b { font-weight: 700; }
  .info-box__phone { font-weight: 700; font-size: 31px; line-height: 1.15; margin-top: 4px; }
  .info-box__hours { font-size: 13px; }
  .coupon {
    position: absolute; left: 736px; top: 165px; width: 300px; height: 174px;
    background: rgba(255,255,255,0.55); border-radius: 12px; padding: 8px;
  }
  .coupon__inner {
    width: 100%; height: 100%; background: var(--white);
    border: 2px dashed var(--brand-red); border-radius: 8px;
    text-align: center; padding-top: 6px;
  }
  .coupon__value { font-weight: 800; font-size: 58px; color: var(--brand-red); line-height: 1; }
  .coupon__expiry { font-size: 14px; color: #333; margin-top: 6px; }
  .coupon__terms { font-weight: 700; font-size: 18px; color: #222; }
  .coupon__foot { display: flex; align-items: center; gap: 10px; margin: 6px 0 0 12px; text-align: left; }
  .coupon__brand { font-weight: 700; font-size: 12px; color: var(--brand-red); width: 50px; line-height: 1; }
  .coupon__fine { font-size: 10px; color: #444; line-height: 1.3; }
  .headline {
    position: absolute; left: 61px; top: 326px;
    font-family: "Rye", serif; font-size: 54px; line-height: 1;
    background: linear-gradient(180deg, #f6b13a 0%, #ee6a1c 55%, #c9261a 100%);
    -webkit-background-clip: text; background-clip: text; color: transparent;
    filter: drop-shadow(2px 2px 0 rgba(120,30,20,0.45));
  }
  .headline-rule {
    position: absolute; left: 61px; top: 396px; width: 470px; height: 2px;
    background: linear-gradient(90deg, rgba(181,18,27,0) 0%, rgba(181,18,27,0.6) 50%, rgba(181,18,27,0) 100%);
  }
  .pitch { position: absolute; left: 64px; top: 430px; font-family: "Alfa Slab One", serif; line-height: 1; }
  .pitch__line { display: block; text-shadow: 1px 1px 0 rgba(255,255,255,0.7); letter-spacing: 1px; }
  .pitch__line--quick { font-size: 41px; color: var(--brand-red); }
  .pitch__line--prepare { font-size: 32px; color: var(--charcoal); margin-top: 10px; }
  .pitch__line--fresh { font-size: 50px; color: var(--fresh-green); margin-top: 8px; }
  .cta {
    position: absolute; left: 68px; top: 603px; width: 318px; height: 45px;
    background: var(--brand-red); border-radius: 5px;
    font-family: "Alfa Slab One", serif; font-size: 30px; color: var(--white);
    display: flex; align-items: center; justify-content: center; letter-spacing: 1px;
  }
  .website {
    position: absolute; left: 68px; top: 666px;
    font-weight: 700; font-size: 26px; color: var(--maroon);
  }
</style>
</head>
<body>
  <main class="postcard">
    <div class="postcard__photo" role="img" aria-label="Photo of a grilled chicken burrito with rice and beans cut in half, a bowl of fresh salsa behind it on a warm peach table"></div>

    <div class="brand">
      <span class="brand__dot"></span>
      <span class="brand__name">Casa Verde<br>Kitchen</span>
    </div>

    <p class="locator">One block from ORC</p>

    <section class="info-box">
      <p class="info-box__address">218 W. Calle Del Sol, Ventura Hills</p>
      <p class="info-box__center">In the <b>Harvest Market Shopping Center</b>. Next to <b>Corner Drug</b></p>
      <p class="info-box__phone">555.210.4477</p>
      <p class="info-box__hours">Open Everyday 10:30 am to 9pm</p>
    </section>

    <aside class="coupon">
      <div class="coupon__inner">
        <p class="coupon__value">$3 OFF</p>
        <p class="coupon__expiry">Expires 10.5.2016</p>
        <p class="coupon__terms">Any purchase of $6 or more</p>
        <div class="coupon__foot">
          <span class="coupon__brand">Casa Verde</span>
          <span class="coupon__fine">One Coupon Per Person.<br>Not Valid With Other Offers</span>
        </div>
      </div>
    </aside>

    <h1 class="headline">MEXICAN GRILL</h1>
    <div class="headline-rule"></div>

    <p class="pitch">
      <span class="pitch__line pitch__line--quick">QUICK SERVICE</span>
      <span class="pitch__line pitch__line--prepare">PREPARE TO ORDER</span>
      <span class="pitch__line pitch__line--fresh">FRESH FOOD</span>
    </p>

    <div class="cta">ORDER NOW</div>
    <p class="website">www.casaverdekitchen.com</p>
  </main>
</body>
</html>
```